Label design for high quality nutritional supplement brand

We need a new label design for our dietary supplement brand "Morelle" from Germany. We sell high-quality nutritional supplements that help improve overall well-being.

All products in our range should receive the new label. You can find our current design on our homepage morelle-brightfield.com. The new design should be completely redesigned and look modern, fresh, high quality, minimalist and clean. We prefer the colors nude, green and earth tones.

The newly created label should contain our Morelle logo. For this reason you will find this file attached. You will also find our current label, which needs to be renewed, in the appendix.

Colors

Designer to choose colors to be used in the design.

Requirements
Must have
• Morelle logo

```html
<!DOCTYPE html>
<html lang="en">
<head>
<meta charset="utf-8">
<title>Morelle Complex – Multivitamin Label</title>
<link href="https://fonts.googleapis.com/css2?family=Open+Sans:wght@400;600&display=swap" rel="stylesheet">
<style>
  :root {
    --backdrop: #e4e4e4;
    --label-white: #fbfbfb;
    --label-shade: #e9e9e9;
    --ink: #5b5b5b;
    --ink-soft: #6a6a6a;
    --olive-light: #d3cf75;
    --olive: #b7b44a;
    --olive-deep: #93962e;
    --on-olive: #ffffff;
  }
  html, body {
    margin: 0;
    padding: 0;
    width: 1200px;
    height: 800px;
    overflow: hidden;
    background: var(--backdrop);
    font-family: "Open Sans", sans-serif;
  }
  .canvas {
    position: relative;
    width: 1200px;
    height: 800px;
  }
  .label {
    position: absolute;
    left: 320px;
    top: 100px;
    width: 560px;
    height: 600px;
    overflow: hidden;
    background: linear-gradient(90deg, var(--label-shade) 0%, var(--label-white) 30%, var(--label-white) 70%, var(--label-shade) 100%);
  }
  .accent-field {
    position: absolute;
    left: 150px;
    top: 330px;
    width: 410px;
    height: 270px;
    background: linear-gradient(90deg, var(--olive-light) 0%, var(--olive) 55%, var(--olive-deep) 100%);
  }
  .product-title {
    position: absolute;
    left: 74px;
    top: 30px;
    margin: 0;
    font-weight: 600;
    font-size: 68px;
    line-height: 64px;
    color: var(--ink);
    letter-spacing: -0.5px;
  }
  .title-rule {
    position: absolute;
    left: 77px;
    top: 168px;
    width: 64px;
    height: 5px;
    background: var(--olive);
  }
  .product-type {
    position: absolute;
    left: 77px;
    top: 184px;
    margin: 0;
    font-size: 22px;
    font-weight: 400;
    color: var(--ink);
  }
  .product-count {
    position: absolute;
    left: 77px;
    top: 244px;
    margin: 0;
    font-size: 18px;
    color: var(--ink-soft);
  }
  .web-address {
    position: absolute;
    left: 60px;
    top: 384px;
    transform-origin: left top;
    transform: translateX(24px) rotate(90deg);
    font-size: 13px;
    color: var(--ink);
    white-space: nowrap;
    letter-spacing: 0.2px;
  }
  .brand-name {
    position: absolute;
    left: 272px;
    top: 500px;
    margin: 0;
    font-size: 44px;
    font-weight: 400;
    color: var(--on-olive);
    letter-spacing: 0.5px;
  }
</style>
</head>
<body>
<main class="canvas">
  <section class="label">
    <div class="accent-field" role="img" aria-label="Olive decorative band area"></div>

    <h1 class="product-title">Morelle<br>Complex</h1>
    <div class="title-rule"></div>
    <p class="product-type">Multivitamin</p>
    <p class="product-count">90 Capsules</p>

    <span class="web-address">morelle-brightfield.com</span>

    <p class="brand-name">Morelle</p>
  </section>
</main>
</body>
</html>
```